Real Estate Sales Representative need a Billboard

I need a billboard for a Real Estate Sales Representative for Crestvane Harlow & Associates. His name is Marcus Belliveau, Cell number: 613-582-7146. Maybe add in "Best Experience Guaranteed", "Award Winning Top Realtor", "Buying or Selling? Call..."

```html
<!DOCTYPE html>
<html lang="en">
<head>
<meta charset="UTF-8">
<title>Marcus Belliveau – Billboard</title>
<link rel="stylesheet" href="https://fonts.googleapis.com/css2?family=Montserrat:ital,wght@0,400;0,500;0,700;1,900&display=swap">
<style>
  :root {
    --page: #e6e7e9;
    --ink: #111111;
    --red: #e8202a;
    --white: #ffffff;
    --grey-light: #f4f4f4;
    --grey-mid: #d6d6d6;
    --badge: #c4c6ca;
    --label-bg: #ebebeb;
    --suit: #1c1f2b;
    --muted: #333333;
  }
  * { box-sizing: border-box; margin: 0; padding: 0; }
  html, body { width: 1200px; height: 1200px; overflow: hidden; background: var(--page); }
  body { font-family: "Montserrat", Arial, sans-serif; position: relative; }

  .billboard {
    position: absolute; left: 40px; top: 320px;
    width: 1120px; height: 560px;
    background: var(--white);
    overflow: hidden;
    box-shadow: 0 10px 30px rgba(0,0,0,.18);
  }
  .street-photo {
    position: absolute; inset: 0;
    background: linear-gradient(100deg, var(--grey-light) 0%, #e2e2e2 40%, var(--grey-mid) 70%, #ececec 100%);
  }
  .street-photo::after {
    content: ""; position: absolute; left: 0; right: 0; bottom: 0; height: 170px;
    background: linear-gradient(180deg, rgba(255,255,255,0) 0%, rgba(255,255,255,.85) 60%, var(--white) 100%);
  }
  .agent-photo {
    position: absolute; left: 0; top: 40px; width: 300px; height: 520px;
    background: linear-gradient(180deg, #c99a7e 0%, #b8876c 45%, var(--suit) 62%, #151822 100%);
    border-radius: 120px 120px 0 0;
  }

  .headline {
    position: absolute; left: 350px; top: 60px;
    font-weight: 900; font-style: italic;
    font-size: 74px; line-height: 0.98;
    letter-spacing: -1px; text-transform: uppercase;
    color: var(--ink);
  }
  .headline .call { color: var(--red); }

  .contact-box {
    position: absolute; left: 372px; top: 262px;
    width: 620px; height: 130px;
    border: 3px solid var(--red); border-radius: 18px;
  }
  .agent-name {
    position: absolute; left: 60px; top: -30px;
    padding: 0 14px; background: var(--label-bg);
    font-weight: 500; font-size: 44px; line-height: 56px;
    letter-spacing: -0.5px; text-transform: uppercase;
    color: var(--ink); white-space: nowrap;
  }
  .agent-phone {
    position: absolute; left: 24px; top: 28px;
    font-weight: 700; font-size: 86px; line-height: 90px;
    letter-spacing: -2px; color: var(--red); white-space: nowrap;
  }

  .credentials {
    position: absolute; left: 410px; top: 430px;
    display: flex; align-items: center; gap: 38px;
  }
  .award-badge { width: 60px; height: 60px; border-radius: 8px; background: var(--badge); }
  .brokerage { display: flex; flex-direction: column; align-items: center; gap: 4px; }
  .brokerage-row { display: flex; align-items: center; gap: 18px; }
  .brand {
    font-weight: 700; font-size: 22px; color: var(--red); letter-spacing: 0.5px;
  }
  .tagline {
    font-weight: 400; font-size: 12px; line-height: 14px; color: var(--muted);
    text-transform: uppercase; text-align: center;
    border-bottom: 1px solid var(--muted); padding-bottom: 3px;
  }
  .brokerage-legal {
    font-weight: 500; font-size: 10px; line-height: 13px; color: var(--ink); text-align: center;
  }
  .brokerage-legal small { display: block; font-size: 8px; font-weight: 400; }
</style>
</head>
<body>
  <section class="billboard">
    <div class="street-photo" role="img" aria-label="Greyscale photo of a street of suburban houses"></div>
    <div class="agent-photo" role="img" aria-label="Portrait photo of the sales representative in a dark suit and blue shirt"></div>

    <h1 class="headline">Buying or<br>Selling? <span class="call">Call</span></h1>

    <div class="contact-box">
      <p class="agent-name">Marcus Belliveau</p>
      <p class="agent-phone">613.582.7146</p>
    </div>

    <div class="credentials">
      <div class="award-badge" role="img" aria-label="Sales award badge"></div>
      <div class="brokerage">
        <div class="brokerage-row">
          <p class="brand">CRESTVANE</p>
          <p class="tagline">Ontario's<br>Home Advisors</p>
        </div>
        <p class="brokerage-legal">Crestvane Harlow &amp; Associates, Brokerage*<small>Independently Owned &amp; Operated</small></p>
      </div>
      <div class="award-badge" role="img" aria-label="Service award badge"></div>
    </div>
  </section>
</body>
</html>
```